Create a business Card for a Women Owned Business Body Positive Company. The winner we hope to work with on other projects coming up for grand opening for flyers, postcards, email marketing, facebook page, stationary, labels, tshirt design....
We would like if possible in the background of the card a infinity symbol or crown if it fits into the design if not it's ok. But I am open to all suggestions we had alot problems with the our new logo being created this time sad to say :(

Our colors are Royal Purple, Grey, Black Thank you in advance for your talent, you hard work and your submissions!
Delia and Nadine :)
Updates

my Logo is velvet harbor boutique which is purple and has a heart and infinity sign in it and my colors are purple silver and black only of another card i had done nothing else. My logo is VELVET HARBOR BOUTIQUE LOGO

Industry/Entity Type

Retail

Contact Information for Business Card

website: www.velvtharborboutiques.example email: sales@velvetharborboutique.example
Delia Pruett & Nadine Kolb Owners

Font styles to use
Script

Colors
b768aa

Requirements
Must have
• COLORS ARE PURPLE BLACK AND GREY
Nice to have
• INFINITY SIGNING IN THE BACKGROUND

```html
<!DOCTYPE html>
<html lang="en">
<head>
<meta charset="utf-8">
<title>Velvet Harbor Boutique – Business Card</title>
<link rel="stylesheet" href="https://fonts.googleapis.com/css2?family=Cinzel:wght@400;500&family=EB+Garamond:wght@400;500&display=swap">
<style>
  :root {
    --stage: #2b2b2d;
    --royal-purple: #7549a0;
    --card-grey: #e4e3e6;
    --ink: #161616;
    --white: #f4f2f6;
    --card-w: 540px;
    --card-h: 310px;
  }
  * { box-sizing: border-box; margin: 0; padding: 0; }
  html, body {
    width: 1200px; height: 880px; overflow: hidden;
    background: var(--stage);
  }
  .canvas { position: relative; width: 1200px; height: 880px; }

  .card {
    position: absolute;
    width: var(--card-w); height: var(--card-h);
    border-radius: 22px;
    overflow: hidden;
  }

  /* Front side */
  .card--front {
    left: 80px; top: 100px;
    background: var(--royal-purple);
    display: flex; align-items: center; justify-content: center;
  }
  .brand-name {
    font-family: "Cinzel", serif;
    font-weight: 400;
    font-size: 30px;
    letter-spacing: 2px;
    line-height: 1.25;
    text-align: center;
  }
  .card--front .brand-name { color: var(--white); }

  /* Back side */
  .card--back {
    left: 580px; top: 470px;
    background: var(--card-grey);
  }
  .card--back .brand-name {
    color: var(--royal-purple);
    position: absolute; left: 0; right: 0; top: 78px;
  }
  .person {
    position: absolute; left: 0; right: 0; top: 150px;
    text-align: center;
  }
  .person__name {
    font-family: "Cinzel", serif;
    font-size: 17px; letter-spacing: 1px;
    color: var(--royal-purple);
  }
  .person__role {
    font-family: "EB Garamond", serif;
    font-size: 15px; color: var(--ink);
    margin-top: -2px;
  }
  .contact-line {
    position: absolute; left: 0; right: 0; bottom: 34px;
    text-align: center;
    font-family: "EB Garamond", serif;
    font-size: 14px; color: var(--ink);
  }
  .contact-line .label { color: var(--royal-purple); }
  .contact-line .sep { color: var(--royal-purple); margin: 0 5px; }

  .edge-band {
    position: absolute; left: 0; right: 0; bottom: 0; height: 12px;
    display: flex;
  }
  .edge-band__purple { flex: 0 0 62%; background: var(--royal-purple); }
  .edge-band__black { flex: 1; background: var(--ink); }
</style>
</head>
<body>
<main class="canvas">
  <section class="card card--front" aria-label="Card front">
    <p class="brand-name">VELVET HARBOR BOUTIQUE</p>
  </section>

  <section class="card card--back" aria-label="Card back">
    <p class="brand-name">VELVET HARBOR BOUTIQUE</p>
    <div class="person">
      <p class="person__name">ROWAN ELLERY</p>
      <p class="person__role">Founder</p>
    </div>
    <p class="contact-line">
      <span class="label">P:</span>(555) 014-2290<span class="sep">|</span><span class="label">E:</span>hello@velvetharbor.example<span class="sep">|</span><span class="label">W:</span>www.velvetharbor.example
    </p>
    <div class="edge-band">
      <span class="edge-band__purple"></span>
      <span class="edge-band__black"></span>
    </div>
  </section>
</main>
</body>
</html>
```